New Web Site - Professional Cleaning Company

I want to create a new attractive website that acts as an advertisement to visitors to entice them to reach out for more information.
We are a commercial/business janitorial service - with a new logo, would like the font to be complimentary to the font of logo, as well as the color scheme.
Target Market(s)
Commercial buildings, schools & medical buildings
Industry/Entity Type
Janitorial
Coding
Coded - Design and coding required
Number of Pages Required
4 page
Requirements
Must have
- Professionalism, sharp imagery

```html
<!DOCTYPE html>
<html lang="en">
<head>
<meta charset="utf-8">
<title>Harrowgate Facility Services</title>
<link href="https://fonts.googleapis.com/css2?family=Open+Sans:wght@300;400;600;700&family=Rokkitt:wght@500&display=swap" rel="stylesheet">
<style>
:root{
  --brand:#12a3d4;
  --navy:#0d2460;
  --green:#3aa84a;
  --text:#333;
  --muted:#666;
  --panel:#efeeef;
  --footer:#111;
  --white:#fff;
}
*{box-sizing:border-box;margin:0;padding:0}
html,body{width:676px;height:1200px;overflow:hidden}
body{position:relative;font-family:'Open Sans',sans-serif;color:var(--text);background:var(--white)}
.abs{position:absolute}
.topbar{left:0;top:0;width:676px;height:22.5px;background:var(--brand);color:var(--white);font-size:9px}
.topbar .item{position:absolute;top:5.5px;display:flex;align-items:center;gap:6px}
.topbar .sep{position:absolute;left:136px;top:5px;width:1px;height:13px;background:rgba(255,255,255,.7)}
.social-top{position:absolute;right:48px;top:5px;display:flex;gap:8px}
.social-top span{width:11px;height:11px;border-radius:50%;background:rgba(255,255,255,.85)}
.logo{left:48px;top:34px;display:flex;align-items:center;gap:6px;width:140px}
.logo .mark{width:22px;height:22px;border-radius:50%;background:var(--brand);flex:none}
.logo .name{font-size:10px;font-weight:700;color:var(--navy);line-height:1.2}
.nav{top:58px;font-size:9.5px;color:var(--muted)}
.nav.active{color:var(--muted)}
.nav.active::after{content:"";position:absolute;left:-1px;right:-1px;top:15px;height:1.5px;background:var(--green)}
.hero{left:0;top:105px;width:676px;height:359px;background:linear-gradient(100deg,#8d9196 0%,#b9bcbf 30%,#4f8fcf 55%,#c9ccce 75%,#8a9a88 100%)}
.welcome{left:48px;top:229px;width:208px;height:91px;background:rgba(90,90,90,.75);color:var(--white);font-weight:700;font-size:17px;line-height:21.5px;padding:12px 12px;text-transform:uppercase}
.arrow{top:327px;width:22px;height:22px;border-radius:50%;background:rgba(90,90,90,.75)}
.card{top:494px;width:182px;height:185px;border-left:1px dotted #999;border-right:1px dotted #999}
.card .rule{position:absolute;left:6px;top:0;width:169px;height:2px;background:var(--navy)}
.card h2{position:absolute;left:7px;top:10px;font-size:11.3px;font-weight:400;color:#111;white-space:nowrap}
.card .photo{position:absolute;left:6px;top:32px;width:169px;height:84px}
.card p{position:absolute;left:7px;top:128px;width:165px;font-size:8px;font-weight:300;line-height:12px;color:#222}
.card .btn{position:absolute;left:6px;top:165px;width:169px;height:20px;background:var(--brand);color:var(--white);font-size:8px;line-height:20px;padding-left:6px}
.promo{top:713px;width:282px;height:81px;background:#f1f1f1;overflow:hidden;text-align:center}
.promo .tiles{position:absolute;left:0;top:0;width:130px;height:81px;background:linear-gradient(100deg,#f7c64a 0%,#f9d77a 35%,rgba(249,222,140,.35) 75%,rgba(241,241,241,0) 100%)}
.promo h3{position:relative;font-size:16px;font-weight:700;color:#555}
.promo p{position:relative;font-size:7.6px;font-weight:300;color:#444;line-height:12px}
.contact{left:0;top:831px;width:676px;height:324px;background:var(--panel)}
.contact h1{position:absolute;left:61px;top:30px;font-family:'Rokkitt',serif;font-weight:500;font-size:20px;letter-spacing:.5px;color:#111}
.contact .bar{position:absolute;left:48px;top:30px;width:2px;height:25px;background:var(--navy)}
.contact .intro{position:absolute;left:48px;top:73px;width:210px;font-size:8.5px;font-weight:300;line-height:11.8px;color:#333}
.small{position:absolute;left:48px;font-size:7.7px;color:#444}
.small.head{color:#111;font-weight:400}
.detail{position:absolute;left:48px;font-size:7.7px;color:#222;display:flex;align-items:center;gap:8px}
.label{position:absolute;font-size:8px;color:#333}
.field{position:absolute;background:var(--white);border:1px solid #ccc}
.send{position:absolute;left:274px;top:259px;width:107px;height:28px;background:var(--brand);color:var(--white);font-size:8px;text-align:center;line-height:28px}
.footer{left:0;top:1155px;width:676px;height:45px;background:var(--footer);color:var(--white)}
.footer .copy{position:absolute;left:50px;top:16px;font-size:8px;font-weight:600}
.footer .dot{position:absolute;top:12.5px;width:20px;height:20px;border-radius:50%}
</style>
</head>
<body>

<div class="abs topbar">
  <div class="item" style="left:49px">
    <svg width="10" height="10" viewBox="0 0 10 10"><path d="M2 0.5l2 2-1 1.2c.6 1.3 1.6 2.3 2.9 2.9l1.2-1 2 2-1.2 1.6C4.5 8.9 1.1 5.5.5 1.7z" fill="#fff"/></svg>
    <span>1(877)555-0142</span>
  </div>
  <div class="sep"></div>
  <div class="item" style="left:144px">
    <svg width="11" height="8" viewBox="0 0 11 8"><rect width="11" height="8" fill="#fff"/><path d="M0 0l5.5 4.5L11 0" stroke="#12a3d4" fill="none"/></svg>
    <span>info@harrowgate.co</span>
  </div>
  <div class="social-top"><span></span><span></span><span></span><span></span></div>
</div>

<div class="abs logo"><span class="mark"></span><span class="name">Harrowgate Facility Services</span></div>

<div class="abs nav active" style="left:198px">Home</div>
<div class="abs nav" style="left:251px">Cleaning</div>
<div class="abs nav" style="left:313px">Emergency Restoration</div>
<div class="abs nav" style="left:439px">Our Process</div>
<div class="abs nav" style="left:518px">Who We Help</div>
<div class="abs nav" style="left:603px">Repair</div>

<div class="abs hero" role="img" aria-label="Two smiling cleaners in blue uniforms with a vacuum and cleaning cart beside a silver van"></div>
<div class="abs welcome">Welcome to Harrowgate Facility Services</div>
<div class="abs arrow" style="left:49px"><svg width="22" height="22" viewBox="0 0 22 22"><path d="M13 6l-5 5 5 5" stroke="#fff" stroke-width="2" fill="none"/></svg></div>
<div class="abs arrow" style="left:74px"><svg width="22" height="22" viewBox="0 0 22 22"><path d="M9 6l5 5-5 5" stroke="#fff" stroke-width="2" fill="none"/></svg></div>

<div class="abs card" style="left:48px">
  <div class="rule"></div><h2>COMMERCIAL CLEANING</h2>
  <div class="photo" role="img" aria-label="Worker cleaning carpet with a yellow extractor machine" style="background:linear-gradient(135deg,#f1f1f1,#dcdcdc 60%,#b9c7dd)"></div>
  <p>Lorem Ipsum is simply dummy text of the printing and typesetting industry.</p>
  <div class="btn">READ MORE</div>
</div>
<div class="abs card" style="left:248px">
  <div class="rule"></div><h2>BUSINESS JANITORIAL</h2>
  <div class="photo" role="img" aria-label="Janitorial team cleaning a bright office" style="background:linear-gradient(135deg,#e6e8ea,#b8bec6 55%,#4b5566)"></div>
  <p>Lorem Ipsum is simply dummy text of the printing and typesetting industry.</p>
  <div class="btn">READ MORE</div>
</div>
<div class="abs card" style="left:447px">
  <div class="rule"></div><h2>EMERGENCY RESTORATION</h2>
  <div class="photo" role="img" aria-label="Firefighters working amid smoke and flames" style="background:linear-gradient(135deg,#f2a04a,#c9692a 50%,#3a2a22)"></div>
  <p>Lorem Ipsum is simply dummy text of the printing and typesetting industry.</p>
  <div class="btn">READ MORE</div>
</div>

<div class="abs promo" style="left:48px">
  <div class="tiles"></div>
  <h3 style="margin-top:10px">OUR PROCESS</h3>
  <p style="margin-top:4px">how process works, how long,&nbsp; how long before re-entering, speed,<br>attn to detail, scent after finished arrive on time,<br>protect from coming back</p>
</div>
<div class="abs promo" style="left:346px">
  <div class="tiles"></div>
  <h3 style="margin-top:15px;margin-left:-10px">CONTACT US 24/7</h3>
  <h3 style="font-size:19px;font-weight:400;margin-top:4px;margin-left:-20px;color:#666">1 (877) 555 - 0142</h3>
</div>

<div class="abs contact">
  <div class="bar"></div>
  <h1>CONTACT US</h1>
  <p class="intro">If you have any questions or comments about our SERVICE, please fill out this form.&nbsp; We would love to hear from you.</p>
  <div class="small head" style="top:124px">ADDRESS:</div>
  <div class="small" style="top:145px">STREET # 123,</div>
  <div class="small" style="top:159px">CITY NAME</div>
  <div class="small" style="top:174px">COUNTRY NAME</div>
  <div class="small head" style="top:194px">GET IN TOUCH</div>
  <div class="detail" style="top:217px"><svg width="10" height="10" viewBox="0 0 10 10"><path d="M2 0.5l2 2-1 1.2c.6 1.3 1.6 2.3 2.9 2.9l1.2-1 2 2-1.2 1.6C4.5 8.9 1.1 5.5.5 1.7z" fill="#111"/></svg>1 (877) 555 - 0142</div>
  <div class="detail" style="top:233px"><svg width="11" height="10" viewBox="0 0 11 10"><rect x="2" y="0" width="7" height="3" fill="#111"/><rect x="0" y="3" width="11" height="5" rx="1" fill="#111"/><rect x="2.5" y="6" width="6" height="4" fill="#111" stroke="#eee" stroke-width=".6"/></svg>123-456-789</div>
  <div class="detail" style="top:250px"><svg width="11" height="8" viewBox="0 0 11 8"><rect width="11" height="8" fill="#111"/><path d="M0 0l5.5 4.5L11 0" stroke="#eee" fill="none"/></svg>info@harrowgate.co</div>

  <div class="label" style="left:274px;top:33px">Full Name*</div>
  <div class="field" style="left:274px;top:47px;width:169px;height:25px"></div>
  <div class="label" style="left:460px;top:33px">Email *</div>
  <div class="field" style="left:460px;top:47px;width:168px;height:25px"></div>
  <div class="label" style="left:274px;top:89px">Address*</div>
  <div class="field" style="left:274px;top:103px;width:169px;height:25px"></div>
  <div class="label" style="left:460px;top:89px">Country / City*</div>
  <div class="field" style="left:460px;top:103px;width:168px;height:25px"></div>
  <div class="label" style="left:274px;top:147px">Message*</div>
  <div class="field" style="left:274px;top:162px;width:355px;height:81px"></div>
  <div class="send">SEND MESSAGE</div>
</div>

<div class="abs footer">
  <div class="copy">© Copyright 2022 Harrowgate Facility Service</div>
  <span class="dot" style="left:514px;background:#3b5b9a"></span>
  <span class="dot" style="left:538px;background:#1da1f2"></span>
  <span class="dot" style="left:561px;background:#d93025"></span>
  <span class="dot" style="left:584px;background:#5b7fa8"></span>
  <span class="dot" style="left:608px;background:#cc2127"></span>
</div>

</body>
</html>
```